REAL PSYCHIC rear window decal. Mystical, light, positive, spiritual coach vibes

Design a sign for my back car window.
HOT PINK and purple swirly, mystical sign. Eye-catching and classy.
Size 24” x 18”
TEXT:
MARISOL DEANE
Psychic & Medium
Www,.marisoldeane.com
World Renowned for Over 45 Years. (This last line make small at bottom)

*This is not a filled in magnet, it will be transparent.

Target Market(s)

Women

Industry/Entity Type

Spirituality

Font styles to use
Script
Other font styles liked:
• See upload for a font I like

Colors
E54698
E96AAD
F1A4CE
F9D9EA
FCEFF6
A7469A
B969AE
D3A5CF
EDDBEB
F8F0F9
6B429C
8869AF
B7A5CE
E3DAEB
F3F0F8

Requirements
Must have
• Pink purple, classy yet mystical vibe
Nice to have
• Easy to read, but old-timey classic font for “MARISOL DEANE”

```html
<!DOCTYPE html>
<html lang="en">
<head>
<meta charset="utf-8">
<title>Marisol Deane – Psychic &amp; Medium Rear Window Decal</title>
<link rel="stylesheet" href="https://fonts.googleapis.com/css2?family=Yellowtail&family=Playfair+Display:wght@700;900&display=swap">
<style>
  :root {
    --page-bg: #ffffff;
    --hot-pink: #e8336a;
    --pink-soft: #e96aad;
    --deep-purple: #2e2450;
    --mid-purple: #4a3a7a;
    --violet: #6b429c;
    --orb: #8a4fc0;
    --white: #ffffff;
    --shadow: #2a2233;
  }
  html, body {
    margin: 0;
    padding: 0;
    width: 968px;
    height: 1200px;
    overflow: hidden;
    background: var(--page-bg);
  }
  .decal {
    position: absolute;
    left: 34px;
    top: 262px;
    width: 900px;
    height: 675px;
  }
  .decal svg { display: block; width: 100%; height: 100%; }
  .name {
    font-family: "Yellowtail", cursive;
    font-size: 200px;
  }
  .title {
    font-family: "Playfair Display", serif;
    font-weight: 900;
    font-size: 112px;
  }
  .url {
    font-family: "Playfair Display", serif;
    font-weight: 700;
    font-size: 56px;
    fill: var(--white);
  }
  .tagline {
    font-family: "Playfair Display", serif;
    font-weight: 700;
    font-size: 30px;
    fill: var(--white);
  }
</style>
</head>
<body>
  <div class="decal">
    <svg viewBox="0 0 1014 760" xmlns="http://www.w3.org/2000/svg">
      <defs>
        <linearGradient id="swirl-bg" x1="0" y1="0" x2="1" y2="1">
          <stop offset="0" stop-color="#3a2c5e"/>
          <stop offset="0.35" stop-color="#2a2148"/>
          <stop offset="0.65" stop-color="#3f2f6e"/>
          <stop offset="1" stop-color="#2d2550"/>
        </linearGradient>
        <radialGradient id="orb-fill" cx="0.4" cy="0.35" r="0.7">
          <stop offset="0" stop-color="#a05fd2"/>
          <stop offset="1" stop-color="#6a3aa0"/>
        </radialGradient>
      </defs>

      <rect class="backdrop" width="1014" height="760" fill="url(#swirl-bg)"
            role="img" aria-label="Swirling purple marbled background with faint sacred geometry"/>

      <g class="orbs" fill="url(#orb-fill)" opacity="0.75">
        <circle cx="510" cy="20" r="45"/>
        <circle cx="832" cy="52" r="22"/>
        <circle cx="160" cy="368" r="55"/>
        <circle cx="875" cy="372" r="48"/>
        <circle cx="178" cy="700" r="24"/>
      </g>
      <g class="orbit-lines" fill="none" stroke="#7a54b8" stroke-width="2" opacity="0.5">
        <circle cx="507" cy="400" r="330"/>
        <circle cx="178" cy="700" r="38"/>
      </g>

      <g class="name" text-anchor="middle">
        <text x="507" y="292" textLength="860" lengthAdjust="spacingAndGlyphs"
              fill="var(--shadow)" stroke="var(--shadow)" stroke-width="44" stroke-linejoin="round"
              transform="translate(6 8)">Marisol Deane</text>
        <text x="507" y="292" textLength="860" lengthAdjust="spacingAndGlyphs"
              fill="var(--hot-pink)" stroke="var(--hot-pink)" stroke-width="40" stroke-linejoin="round">Marisol Deane</text>
        <text x="507" y="292" textLength="860" lengthAdjust="spacingAndGlyphs"
              fill="var(--white)" stroke="var(--white)" stroke-width="26" stroke-linejoin="round">Marisol Deane</text>
        <text x="507" y="292" textLength="860" lengthAdjust="spacingAndGlyphs"
              fill="var(--hot-pink)">Marisol Deane</text>
      </g>

      <g class="title" text-anchor="middle">
        <text x="495" y="412" fill="var(--shadow)" stroke="var(--shadow)" stroke-width="14" stroke-linejoin="round" transform="translate(4 5)">Psychic &amp;</text>
        <text x="495" y="412" fill="var(--white)" stroke="var(--hot-pink)" stroke-width="10" stroke-linejoin="round" paint-order="stroke">Psychic &amp;</text>
        <text x="492" y="530" fill="var(--shadow)" stroke="var(--shadow)" stroke-width="14" stroke-linejoin="round" transform="translate(4 5)">Medium</text>
        <text x="492" y="530" fill="var(--white)" stroke="var(--hot-pink)" stroke-width="10" stroke-linejoin="round" paint-order="stroke">Medium</text>
      </g>

      <g class="url-band">
        <rect x="125" y="590" width="765" height="84" rx="42" fill="var(--hot-pink)"/>
        <rect x="135" y="594" width="745" height="40" rx="20" fill="var(--pink-soft)" opacity="0.35"/>
        <text class="url" x="507" y="650" text-anchor="middle" textLength="620" lengthAdjust="spacingAndGlyphs">www.marisoldeane.com</text>
      </g>

      <text class="tagline" x="507" y="718" text-anchor="middle">World Renowned for Over 45 Years</text>
    </svg>
  </div>
</body>
</html>
```